Flyer Design & Business Cards

I have tried to make up some flyer and have attached them as info with what we would like included. I would like them made to look more professional and I would like business cards along the same line.

Industry/Entity Type

Business

```html
<!DOCTYPE html>
<html lang="en">
<head>
<meta charset="utf-8">
<title>Eastholm Inn – Flyer</title>
<link href="https://fonts.googleapis.com/css2?family=Didact+Gothic&family=Montserrat:wght@700&display=swap" rel="stylesheet">
<style>
  :root {
    --charcoal: #1f2428;
    --rope: #d9dcdf;
    --rope-shade: #9ea4aa;
    --white: #ffffff;
    --orange: #f39a1e;
    --footer-blue: #1a62a6;
    --photo-warm: #6b3a1c;
    --photo-glow: #c7782e;
    --ship-white: rgba(255,255,255,0.9);
  }
  * { margin: 0; padding: 0; box-sizing: border-box; }
  html, body { width: 853px; height: 1200px; overflow: hidden; background: var(--charcoal); }
  .flyer {
    position: relative;
    width: 853px;
    height: 1200px;
    background: var(--charcoal);
    font-family: "Didact Gothic", "Century Gothic", sans-serif;
    color: var(--white);
    overflow: hidden;
  }
  .photo-strip {
    position: absolute; left: 0; top: 0; width: 853px; height: 205px;
    display: flex;
  }
  .photo-strip .photo { flex: 1; }
  .photo--bar { background: linear-gradient(160deg, #3a2412, var(--photo-glow) 55%, #2a1a0d); }
  .photo--food { background: radial-gradient(circle at 50% 50%, #e8d9c2 0 35%, #7a5a3a 36%, #3b2616 100%); }
  .photo--fire { background: radial-gradient(circle at 55% 60%, #f0a040 0 12%, #7a3c18 30%, #2b1b12 80%); }
  .photo--taps { background: linear-gradient(200deg, #2a1a10, var(--photo-warm) 50%, #b24a1c); }

  .rope-band {
    position: absolute; left: 0; width: 853px;
    background: linear-gradient(180deg, var(--rope-shade), var(--rope) 50%, var(--rope-shade));
  }
  .rope-band--top-a { top: 214px; height: 40px; }
  .rope-band--top-b { top: 262px; height: 40px; }
  .rope-band--bottom { top: 992px; height: 44px; }

  .headline {
    position: absolute; top: 322px; left: 0; width: 853px;
    text-align: center; font-size: 56px; font-weight: 400; letter-spacing: 0.3px; line-height: 1;
  }
  .offer-line {
    position: absolute; top: 394px; left: 0; width: 853px;
    text-align: center;
    font-family: "Montserrat", "Arial", sans-serif; font-weight: 700;
    font-size: 34px; color: var(--orange); letter-spacing: 0.3px; line-height: 1;
  }
  .offer-line .dot { font-size: 30px; margin: 0 6px; }

  .ship-illustration {
    position: absolute; left: 500px; top: 700px; width: 330px; height: 330px;
    background: radial-gradient(ellipse at 55% 55%, var(--ship-white) 0 30%, rgba(255,255,255,0.55) 55%, rgba(255,255,255,0) 75%);
    opacity: 0.85;
  }

  .intro {
    position: absolute; left: 60px; top: 446px; width: 420px;
    font-size: 21px; line-height: 29px;
  }
  .intro p + p { margin-top: 29px; }

  .brand-sign {
    position: absolute; left: 520px; top: 447px; width: 253px; height: 209px;
    display: flex; align-items: center; justify-content: center;
  }
  .brand-name {
    font-size: 46px; color: var(--orange); text-align: center; line-height: 1.05;
  }
  .established {
    position: absolute; left: 520px; top: 665px; width: 253px;
    text-align: center; font-size: 18px;
  }

  .footer {
    position: absolute; left: 0; top: 1043px; width: 853px; height: 157px;
    background: var(--footer-blue); text-align: center;
  }
  .footer .web-row {
    margin-top: 24px; display: flex; justify-content: center; align-items: center; gap: 14px;
  }
  .social-square { width: 34px; height: 34px; background: #cfe3f4; border-radius: 6px; }
  .website {
    font-family: "Montserrat", "Arial", sans-serif; font-weight: 700;
    font-size: 40px; color: var(--orange); line-height: 1;
  }
  .address, .phone { font-size: 17px; line-height: 29px; }
  .address { margin-top: 10px; }
</style>
</head>
<body>
<div class="flyer">
  <div class="photo-strip" role="img" aria-label="Photographs of the bar: pints of real ale, a plate of bar food, a wood-burning stove and beer taps">
    <div class="photo photo--bar"></div>
    <div class="photo photo--food"></div>
    <div class="photo photo--fire"></div>
    <div class="photo photo--taps"></div>
  </div>

  <div class="rope-band rope-band--top-a" role="img" aria-label="Twisted rope border"></div>
  <div class="rope-band rope-band--top-b" role="img" aria-label="Twisted rope border"></div>

  <h1 class="headline">The only pub in North Uist</h1>
  <div class="offer-line"><span class="dot">•</span>REAL ALES <span class="dot">•</span>BAR FOOD <span class="dot">•</span>LIVE MUSIC</div>

  <div class="ship-illustration" role="img" aria-label="White illustration of a tall sailing ship on the waves"></div>

  <div class="intro">
    <p>Eastholm Inn is a Georgian listed building located on the west side of North Uist, on the edge of the Atlantic, owned and run by Morag and Alasdair Grant.</p>
    <p>"Eastholm" is a friendly pub with a traditional Hebridean atmosphere and stocks an extensive range of drinks including real ales from Harbour Brewery. We offer a variety of home-cooked food including local produce when available.</p>
    <p>Facilities: TV, Free Wi-Fi, pool table, darts, table games and outdoor games. There is outdoor seating for sunny days/evenings.</p>
  </div>

  <div class="brand-sign">
    <div class="brand-name">Eastholm<br>Inn</div>
  </div>
  <div class="established">Established 1896</div>

  <div class="rope-band rope-band--bottom" role="img" aria-label="Twisted rope border"></div>

  <footer class="footer">
    <div class="web-row">
      <span class="social-square"></span>
      <span class="website">www.eastholminn.com</span>
      <span class="social-square"></span>
    </div>
    <div class="address">Eastholm Inn, Shore Road, Baleshare, North Uist HS6 9ZQ</div>
    <div class="phone">Telephone: 01876 500123</div>
  </footer>
</div>
</body>
</html>
```